Webdesign für Vermietung eines Ferienhauses auf der Insel Usedom
Zielgruppe
Vermietung eines Ferienhauses auf der Insel Usedom
ZG: Urlauber im gehobenem Preissegment, die Luxus schätzen und urlauben wollen
Aufgabenstellung
- IN ADOBE PHOTOSHOP
- Bilder können hier entnommen werden: https://www.quartiro-net.example/ob-link-ansicht-reserve/index.php?portal=48127&unit=39502/index.html
- gern können Sie auch Stock-Bilder verwenden
- Der Buchungskalender /die Verfügbarkeit der freien Zeiträume soll präsent im oberen Bereich der Seite stehen
- Lumivo-Bewertungsbutton
- Es gibt kein Logo - bitte den Namenszug 'KIEFERNVILLA*****HOLMSTEDE' nutzen

```html
<!DOCTYPE html>
<html lang="de">
<head>
<meta charset="utf-8">
<title>Kiefernvilla Holmstede – Ferienhaus auf Usedom</title>
<link href="https://fonts.googleapis.com/css2?family=Inter:wght@400;500;600;700&display=swap" rel="stylesheet">
<style>
:root{
  --page:#f7f8fa;
  --white:#ffffff;
  --navy:#1f2a3a;
  --gold:#d9a443;
  --ink:#1d2430;
  --muted:#6b7280;
  --line:#2c3a4e;
  --soft:#f4f4f4;
}
*{box-sizing:border-box;margin:0;padding:0}
html,body{width:1200px;height:2910px;overflow:hidden}
body{background:var(--page);font-family:'Inter',sans-serif;color:var(--ink)}
.site{position:absolute;left:117px;top:99px;width:963px;height:2710px;background:var(--white);box-shadow:0 20px 60px rgba(30,40,60,.08);overflow:hidden}
.abs{position:absolute}
.hero{left:0;top:0;width:963px;height:452px;background:linear-gradient(180deg,#2b56b8 0%,#5b7fc4 35%,#8a8b7f 60%,#3c4a2c 100%)}
.brand{display:flex;align-items:center;gap:9px;font-weight:500;font-size:15px;color:var(--white)}
.brand-dot{width:18px;height:18px;border-radius:50%;background:var(--gold)}
.nav{left:331px;top:20px;display:flex;gap:22px;font-size:10px;color:var(--white)}
.btn-book{left:806px;top:13px;width:82px;height:28px;background:var(--gold);color:var(--white);font-size:10px;display:flex;align-items:center;justify-content:center}
.dots{left:462px;top:390px;display:flex;gap:7px}
.dots span{width:5px;height:5px;border-radius:50%;background:var(--white)}
.dots span.off{opacity:.5}
.booking{left:75px;top:412px;width:813px;height:89px;background:var(--navy);box-shadow:0 10px 25px rgba(0,0,0,.2)}
.field{position:absolute;top:22px}
.field label{display:block;font-size:9px;color:#d6dbe3;margin-bottom:5px}
.field .box{height:28px;border:1px solid #c9ced6;display:flex;align-items:center;padding:0 9px;gap:7px;font-size:10px;color:var(--white)}
.field svg{flex:none}
.field .chev{margin-left:auto}
.dash{position:absolute;left:166px;top:50px;font-size:9px;color:#c9ced6}
.btn-check{left:650px;top:39px;width:141px;height:28px;background:var(--gold);color:var(--white);font-size:10px;font-weight:500;display:flex;align-items:center;justify-content:center}
.mark{width:20px;height:20px;border-radius:50%;border:2px solid var(--gold)}
.section-title{font-size:21px;font-weight:600;text-align:center;width:963px;left:0}
.intro{left:148px;top:640px;width:666px;text-align:center;font-size:11px;line-height:16px;color:#333a45}
.card{position:absolute;top:866px;width:256px}
.card .photo{width:256px;height:228px}
.card h3{font-size:14px;font-weight:600;margin-top:16px}
.card p{font-size:10.5px;line-height:16px;color:var(--muted);margin-top:8px}
.btn-more{display:flex;align-items:center;justify-content:center;width:81px;height:29px;border:1px solid var(--navy);font-size:11px;margin-top:12px}
.video{left:0;top:1331px;width:963px;height:412px;background:linear-gradient(135deg,#3e5a2c 0%,#6b7a5a 45%,#5a6b46 70%,#2f4a24 100%)}
.lage-title{left:75px;top:1872px;font-size:21px;font-weight:600}
.lage-text{left:75px;top:1914px;width:330px;font-size:11px;line-height:16px;color:#333a45}
.map{left:492px;top:1830px;width:396px;height:289px;background:linear-gradient(110deg,#bfe3c6 0%,#c9e6cf 50%,#9fc2f2 62%,#95bcf4 100%)}
.contact{left:0;top:2199px;width:963px;height:288px;background:var(--soft)}
.contact h2{position:absolute;left:75px;top:50px;font-size:21px;font-weight:600}
.contact .lead{position:absolute;left:75px;top:84px;width:240px;font-size:9px;line-height:14px;color:var(--muted)}
.contact .info{position:absolute;left:75px;top:140px;font-size:10.5px;line-height:19px}
.contact .mark{position:absolute;left:75px;top:221px}
.form-label{position:absolute;font-size:9px;color:#333a45}
.form-input{position:absolute;height:32px;border:1px solid var(--navy);background:var(--white)}
.agree{position:absolute;left:568px;top:183px;display:flex;align-items:center;gap:8px;font-size:9.5px}
.agree span.chk{width:13px;height:13px;border:1px solid var(--navy);background:var(--white)}
.btn-send{position:absolute;left:568px;top:212px;width:99px;height:32px;background:var(--gold);color:var(--white);font-size:11px;display:flex;align-items:center;justify-content:center}
.footer{left:0;top:2487px;width:963px;height:223px;background:var(--navy);color:var(--white)}
.footer .lead{position:absolute;left:75px;top:88px;width:240px;font-size:9px;line-height:14px;color:#a4adbb}
.footer .follow{position:absolute;left:75px;top:145px;font-size:9px;color:#c9ced6}
.social{position:absolute;left:75px;top:165px;display:flex;gap:14px;font-size:9px;color:var(--white)}
.fnav{position:absolute;top:46px;font-size:9.5px;color:#a4adbb;line-height:23px}
.fnav strong{display:block;color:var(--white);font-weight:600;font-size:10px;margin-bottom:8px}
</style>
</head>
<body>
<div class="site">
  <div class="abs hero" role="img" aria-label="Foto: reetgedecktes Ferienhaus mit Holzfassade zwischen Kiefern unter blauem Himmel"></div>
  <div class="abs brand" style="left:75px;top:17px"><span class="brand-dot"></span>Kiefernvilla Holmstede</div>
  <nav class="abs nav"><span>Das 5* Strandhaus</span><span>Verfügbarkeit</span><span>Die Räumlichkeiten</span><span>Lage</span><span>Kontakt</span></nav>
  <div class="abs btn-book">Jetzt buchen</div>
  <div class="abs dots"><span class="off"></span><span class="off"></span><span class="off"></span><span></span><span></span><span></span></div>

  <div class="abs booking">
    <div class="field" style="left:21px;width:139px"><label>Einchecken</label>
      <div class="box"><svg width="11" height="11" viewBox="0 0 12 12" fill="none" stroke="#fff" stroke-width="1"><rect x="1" y="2" width="10" height="9"/><path d="M1 5h10M4 1v2M8 1v2"/></svg>Von</div></div>
    <span class="dash">-</span>
    <div class="field" style="left:181px;width:138px"><label>Kasse</label>
      <div class="box"><svg width="11" height="11" viewBox="0 0 12 12" fill="none" stroke="#fff" stroke-width="1"><rect x="1" y="2" width="10" height="9"/><path d="M1 5h10M4 1v2M8 1v2"/></svg>19. 11. 2022</div></div>
    <div class="field" style="left:335px;width:141px"><label>Erwachsene</label>
      <div class="box"><svg width="11" height="11" viewBox="0 0 12 12" fill="none" stroke="#fff" stroke-width="1"><circle cx="6" cy="4" r="2.5"/><path d="M1.5 11c0-2.5 2-4 4.5-4s4.5 1.5 4.5 4"/></svg>2 Erw.<svg class="chev" width="9" height="6" viewBox="0 0 9 6" fill="none" stroke="#fff"><path d="M1 1l3.5 3.5L8 1"/></svg></div></div>
    <div class="field" style="left:492px;width:141px"><label>Kinder</label>
      <div class="box"><svg width="11" height="11" viewBox="0 0 12 12" fill="none" stroke="#fff" stroke-width="1"><circle cx="6" cy="4" r="2.5"/><path d="M1.5 11c0-2.5 2-4 4.5-4s4.5 1.5 4.5 4"/></svg>1<svg class="chev" width="9" height="6" viewBox="0 0 9 6" fill="none" stroke="#fff"><path d="M1 1l3.5 3.5L8 1"/></svg></div></div>
    <div class="abs btn-check">Jetzt prüfen</div>
  </div>

  <div class="abs mark" style="left:471px;top:556px"></div>
  <h1 class="abs section-title" style="top:596px">Das 5* Strandhaus</h1>
  <p class="abs intro"><strong>Kiefernvilla Holmstede</strong> ist eine in Mecklenburg-Vorpommern einzigartige 5-Sterne-Ferienhaus-Anlage mit 42 großzügigen, schilfrohrgedeckten Strandhäusern mit bis zu 225 m² Wohnfläche und 26 Ferienwohnungen. Grundstücke mit bis zu 3300 m² Fläche bieten viel Platz zum Wohlfühlen. Dieses exklusive, 2017 erbaute Strandhaus mit ca. 145 m² Wohnfläche und einem Grundstück von ca. 700 m² befindet sich ca. 5 Gehminuten vom Strand entfernt.Das Haus verfügt über beheizbarer Aussenwhirlpool (ganzjährig nutzbar), Safe, Internet - WLAN, Sauna mit Infrarot, 2 Terrassen, HWR mit Waschmaschine und Trockner, Bollerwagen, Parkplatz.</p>

  <h2 class="abs section-title" style="top:820px">Die Räumlichkeiten</h2>
  <div class="card" style="left:75px">
    <div class="photo" role="img" aria-label="Foto: heller Wellnessbereich mit zwei Holzliegen und Blick in den Garten" style="background:linear-gradient(135deg,#e9ece8,#c9b79a 60%,#3aa6a8)"></div>
    <h3>Erdgeschoss</h3>
    <p>1 Schlafraum mit Doppelbett (2,00 x 1,80 m), großzügiger Wellnessbereich mit Sauna undInfrarot, Ruhebereich, bodentiefe Dusche, separates WC, HWR mit Waschmaschine und Trockner</p>
    <div class="btn-more">Mehr</div>
  </div>
  <div class="card" style="left:353px">
    <div class="photo" role="img" aria-label="Foto: Wohn- und Essbereich mit weißem Tisch und grauem Sofa" style="background:linear-gradient(135deg,#f1efea,#d8d2c6 55%,#6f6c66)"></div>
    <h3>Obergeschoss</h3>
    <p>1 Schlafraum mit Doppelbett (2,20 x 1,80 m), Einzelbett und Kinderreisebett (BETTLO), 1 Schlafraum mit Doppelbett (2,00 x 1,80 m), Badezimmer mit Dusche, Badewanne, WC, Fön</p>
    <div class="btn-more">Mehr</div>
  </div>
  <div class="card" style="left:631px">
    <div class="photo" role="img" aria-label="Foto: sprudelnder Außenwhirlpool vor dem Haus und Garten" style="background:linear-gradient(180deg,#6a9bd8 0%,#9aa88a 40%,#5c8a3c 60%,#cfd8dc 80%,#8a7a6a)"></div>
    <h3>Familienfreundlich</h3>
    <p>Das exklusive, schilfrohrgedeckte, 2017 erbaute Strandhaus mit ca. 145 m2&nbsp; Wohnfläche und einem Grundstück von ca. 700 m2 befindet sich in der nähe eines Naturschutzgebietes, ca. 5 Gehminuten vom Strand entfernt</p>
    <div class="btn-more">Mehr</div>
  </div>

  <div class="abs video" role="img" aria-label="Video-Standbild: Luftaufnahme der Ferienhaussiedlung im Kiefernwald"></div>
  <svg class="abs" style="left:469px;top:1523px" width="24" height="28" viewBox="0 0 24 28" fill="none" stroke="#fff" stroke-width="1.5"><path d="M2 2l20 12L2 26z"/></svg>

  <div class="abs mark" style="left:75px;top:1832px"></div>
  <h2 class="abs lage-title">Lage</h2>
  <p class="abs lage-text"><strong>Kiefernvilla Holmstede</strong> ist eine in Mecklenburg-Vorpommern einzigartige 5-Sterne-Ferienhaus-Anlage mit 42 großzügigen, schilfrohrgedeckten Strandhäusern mit bis zu 225 m² Wohnfläche und 26 Ferienwohnungen. Dieses exklusive, 2017 erbaute Strandhaus mit ca. 145 m² Wohnfläche und einem Grundstück von ca. 700 m² befindet sich ca. 5 Gehminuten vom Strand entfernt.</p>
  <div class="abs map" role="img" aria-label="Karte: Lage des Ferienhauses an der Ostseeküste"></div>

  <section class="abs contact">
    <h2>Kontaktiere uns</h2>
    <p class="lead">Faucibus urna sed eget sit egestas sed malesuada. Purus lorem eget enim mattis lorem elit. Elit volutpat iaculis tortor sagittis mi sagittis ultricies accumsan.</p>
    <p class="info">+48 912 555 204<br>info@kiefernvillaholmstede</p>
    <div class="mark"></div>
    <span class="form-label" style="left:568px;top:45px">Vorname</span>
    <div class="form-input" style="left:568px;top:61px;width:149px"></div>
    <span class="form-label" style="left:738px;top:45px">Nachname</span>
    <div class="form-input" style="left:738px;top:61px;width:150px"></div>
    <span class="form-label" style="left:568px;top:111px">E-mail</span>
    <div class="form-input" style="left:568px;top:127px;width:320px"></div>
    <div class="agree"><span class="chk"></span>Sie stimmen unserer freundlichen Datenschutzerklärung zu.</div>
    <div class="btn-send">Senden</div>
  </section>

  <footer class="abs footer">
    <div class="abs brand" style="left:75px;top:46px;font-size:16px"><span class="brand-dot"></span>Kiefernvilla Holmstede</div>
    <p class="lead">Faucibus urna sed eget sit egestas sed malesuada. Purus lorem eget enim mattis lorem elit. Elit volutpat iaculis tortor sagittis mi sagittis ultricies accumsan.</p>
    <span class="follow">Folgen Sie uns</span>
    <div class="social"><span>Netzpost</span><span>Treffpunkt</span><span>Bildkreis</span></div>
    <div class="fnav" style="left:638px"><strong>Navigation</strong>Das 5* Strandhaus<br>Verfügbarkeit<br>Die Räumlichkeiten<br>Lage<br>Kontakt</div>
    <div class="fnav" style="left:787px">Impressum<br>Datenschutz</div>
  </footer>
</div>
</body>
</html>
```